Vell Partners Building Business Cards

We need a business card that reflects our business as "Solar Experts" in San Diego. Browse our website www.vellpartners.example our License needs to be displayed as "CSLB# 4718392" our phone number is (619) 555-0147

Save thousands on your electric bills and increase the value of your home while helping to protect the environment. Our solar installation experts will help you design the system that's right for you, using only the highest quality equipment that will look great and give you ideal performance. Our goal is to make you energy independent, and get your electric bill to 0.

Tobias Wrenfield
(619) 555-0147
tobias@vellpartners.example

Target Market(s)

Home owners in san diego looking for solar

Industry/Entity Type

Solar Energy

Contact Information for Business Card

Tobias Wrenfield
(619) 555-0147
tobias@vellpartners.example

Font styles to use
Other font styles liked:
• Use our logo font

Requirements
Must have
• License needs to be displayed as "CSLB# 4718392" our phone number is (619) 555-0147
Nice to have
• Real images of rooftop home solar in san diego
Should not have
• our business address

```html
<!DOCTYPE html>
<html lang="en">
<head>
<meta charset="utf-8">
<title>Vell Partners Building – Business Card</title>
<link rel="stylesheet" href="https://fonts.googleapis.com/css2?family=Lora:wght@400;700&display=swap">
<style>
  :root {
    --navy: #1f3f78;
    --navy-deep: #2b4a86;
    --navy-soft: #3a5995;
    --gold: #f5ae1f;
    --white: #ffffff;
    --backdrop: #222222;
  }
  * { margin: 0; padding: 0; box-sizing: border-box; }
  html, body { width: 1189px; height: 1200px; overflow: hidden; }
  body {
    background: var(--backdrop);
    font-family: "Lora", Georgia, serif;
    position: relative;
  }
  .card {
    position: absolute;
    left: 171px;
    width: 856px;
    height: 488px;
    overflow: hidden;
  }
  .card--front { top: 67px; }
  .card--back { top: 626px; background: var(--white); }

  .front-photo {
    position: absolute; inset: 0;
    background: linear-gradient(135deg, var(--navy-soft) 0%, var(--navy-deep) 55%, #34548f 100%);
  }
  .front-brand {
    position: absolute; left: 0; right: 0; top: 212px;
    text-align: center;
    font-weight: 700;
    font-size: 54px;
    line-height: 1;
    color: var(--white);
    letter-spacing: -0.5px;
  }
  .social-row {
    position: absolute; top: 335px; left: 0; right: 0;
    display: flex; justify-content: center; gap: 20px;
  }
  .social-row span {
    width: 34px; height: 34px; background: var(--white); border-radius: 2px;
  }

  .sun-illustration {
    position: absolute; left: 0; top: 84px;
    width: 372px; height: 376px;
    background: linear-gradient(180deg, var(--gold) 0%, var(--gold) 50%, var(--navy) 100%);
    border-top-right-radius: 60% 40%;
  }
  .back-brand {
    position: absolute; right: 43px; top: 70px;
    font-weight: 700; font-size: 40px;
    line-height: 1;
    color: var(--navy);
    letter-spacing: -0.5px;
    white-space: nowrap;
  }
  .license {
    position: absolute; right: 43px; top: 163px;
    font-size: 21px; line-height: 1.2; color: var(--navy);
  }
  .person-name {
    position: absolute; left: 431px; top: 280px;
    font-size: 29px; line-height: 1.2; font-weight: 700; color: var(--navy);
  }
  .contact-list {
    position: absolute; left: 431px; top: 348px;
    list-style: none;
  }
  .contact-list li {
    display: flex; align-items: center; gap: 12px;
    height: 34px;
    font-size: 23px; color: var(--navy);
    white-space: nowrap;
  }
  .contact-icon {
    width: 29px; height: 29px; background: var(--gold);
    display: flex; align-items: center; justify-content: center;
    flex: none;
  }
</style>
</head>
<body>
  <section class="card card--front">
    <div class="front-photo" role="img" aria-label="Photo of rooftop solar panels under a blue tint"></div>
    <div class="front-brand">Vell Partners Building</div>
    <div class="social-row" aria-label="Social media links">
      <span></span><span></span><span></span><span></span>
    </div>
  </section>

  <section class="card card--back">
    <div class="sun-illustration" role="img" aria-label="Large illustration of a rising sun over ocean waves"></div>
    <div class="back-brand">Vell Partners Building</div>
    <div class="license">CSLB# 4718392</div>
    <div class="person-name">Tobias Wrenfield</div>
    <ul class="contact-list">
      <li>
        <span class="contact-icon">
          <svg width="18" height="18" viewBox="0 0 24 24"><path fill="#fff" d="M6.6 10.8a15 15 0 0 0 6.6 6.6l2.2-2.2a1 1 0 0 1 1-.25 11.4 11.4 0 0 0 3.6.57 1 1 0 0 1 1 1V20a1 1 0 0 1-1 1A17 17 0 0 1 3 4a1 1 0 0 1 1-1h3.5a1 1 0 0 1 1 1c0 1.25.2 2.45.57 3.570a1 1 0 0 1-.25 1z"/></svg>
        </span>
        (619) 555-0147
      </li>
      <li>
        <span class="contact-icon">
          <svg width="18" height="14" viewBox="0 0 18 14"><rect x="1" y="1" width="16" height="12" fill="none" stroke="#fff" stroke-width="1.6"/><path d="M1 1l8 7 8-7" fill="none" stroke="#fff" stroke-width="1.6"/></svg>
        </span>
        tobias@vellpartners.example
      </li>
      <li>
        <span class="contact-icon">
          <svg width="18" height="18" viewBox="0 0 20 20" fill="none" stroke="#fff" stroke-width="1.4"><circle cx="10" cy="10" r="8"/><ellipse cx="10" cy="10" rx="3.5" ry="8"/><path d="M2 10h16M3.5 6h13M3.5 14h13"/></svg>
        </span>
        www.vellpartners.example
      </li>
    </ul>
  </section>
</body>
</html>
```